Direct Mail Letter / Reply Device / Outer Envelope

I'm interested in seeing if I can give my charity's annual appeal a fresh look and feel. I have written the letter though edits might be needed. We're really looking for 'pop'. Edits to the letter will need to happen before our final design. My budget for design is about $250.00 but I may be able to negotiate for the right design.

Target Market(s)

Donors to a specific charity

Font styles to use
Serif
Sans Serif

Colors

Designer to choose colors to be used in the design.

Requirements
Must have
• Color photos that make the most of the photos I have regardless of resolutions. I need something in a format that will let me make edits and / or reuse next year or for my thank you letter. Basically, a Word friendly version.

```html
<!DOCTYPE html>
<html lang="en">
<head>
<meta charset="utf-8">
<title>Retriever Haven – Annual Appeal Letter, Page 2</title>
<link rel="stylesheet" href="https://fonts.googleapis.com/css2?family=Work+Sans:wght@300;400;700&family=Caveat:wght@400&display=swap">
<style>
  :root{
    --teal-deep:#1f8fa3;
    --teal:#2a9fb3;
    --teal-light:#5ec3d2;
    --ink:#1d1d1d;
    --body:#3a3a3a;
    --muted:#8c9497;
    --rule:#7f8f93;
    --mist:#e9f1ef;
    --paper:#ffffff;
  }
  *{margin:0;padding:0;box-sizing:border-box;}
  html,body{width:849px;height:1200px;overflow:hidden;background:var(--paper);}
  .page{position:relative;width:849px;height:1200px;overflow:hidden;background:var(--paper);
    font-family:"Work Sans",Arial,sans-serif;color:var(--body);}
  .header-band{position:absolute;left:0;top:0;width:849px;height:320px;}
  .backdrop-shape{position:absolute;left:430px;top:620px;width:460px;height:600px;}
  .portrait{position:absolute;left:106px;top:58px;width:256px;height:256px;}
  .caption{position:absolute;left:430px;top:116px;font-family:"Caveat",cursive;
    font-size:40px;color:#eef8fa;letter-spacing:1px;}
  .letter-body{position:absolute;left:154px;top:380px;width:546px;
    font-size:15.3px;font-weight:300;line-height:24.9px;}
  .letter-body p{margin-bottom:8.5px;}
  .letter-body strong{font-weight:700;color:var(--ink);}
  .footer{position:absolute;left:154px;top:1082px;width:542px;border-top:1px solid var(--rule);
    text-align:center;font-size:13px;color:var(--muted);}
  .footer .contact{margin-top:12px;}
  .footer .web{margin-top:7px;font-weight:700;color:#555c5f;}
</style>
</head>
<body>
<div class="page">
  <svg class="header-band" viewBox="0 0 849 320" aria-hidden="true">
    <polygon points="0,0 849,0 849,300 365,180 240,150 0,172" fill="var(--teal)"/>
    <polygon points="0,0 520,0 0,90" fill="var(--teal-deep)" opacity=".55"/>
    <polygon points="0,90 180,125 0,172" fill="var(--teal-light)" opacity=".35"/>
    <polygon points="520,0 849,0 849,200" fill="var(--teal-light)" opacity=".35"/>
  </svg>

  <svg class="backdrop-shape" viewBox="0 0 460 600" role="img" aria-label="Faint background decoration">
    <defs>
      <radialGradient id="mistGlow" cx="55%" cy="50%" r="60%">
        <stop offset="0" stop-color="var(--mist)"/>
        <stop offset="1" stop-color="var(--mist)" stop-opacity="0"/>
      </radialGradient>
    </defs>
    <rect width="460" height="600" fill="url(#mistGlow)"/>
  </svg>

  <svg class="portrait" viewBox="0 0 256 256" role="img" aria-label="Photo of Helen, a chocolate Labrador wearing a blue bandana, lying on a mat with toys">
    <defs>
      <linearGradient id="photoTone" x1="0" y1="0" x2="1" y2="1">
        <stop offset="0" stop-color="#6b4232"/>
        <stop offset=".55" stop-color="#cdb9a4"/>
        <stop offset="1" stop-color="#e8ddcc"/>
      </linearGradient>
    </defs>
    <circle cx="128" cy="128" r="128" fill="var(--paper)"/>
    <circle cx="128" cy="128" r="121" fill="url(#photoTone)"/>
  </svg>

  <svg style="position:absolute;left:255px;top:88px" width="170" height="60" viewBox="0 0 170 60" aria-hidden="true">
    <path d="M160 52 C140 20 100 5 70 12 C50 16 35 25 22 38" fill="none" stroke="#cfe3ea" stroke-width="3" stroke-linecap="round"/>
    <path d="M18 24 L20 42 L36 40" fill="none" stroke="#cfe3ea" stroke-width="3" stroke-linecap="round" stroke-linejoin="round"/>
  </svg>
  <div class="caption">'Helen'</div>

  <div class="letter-body">
    <p>care for almost 18 months until she found a family who could meet her special needs.</p>
    <p>Since the end of the economic crisis, <strong>our average cost to save a lab has increased from $650 per dog to more than $750.</strong> Many dogs require so much more than routine care.</p>
    <p>Early in 2017, we rescued Ramsey, a Lab already dependent on a wheelchair. He was given weeks to live, maybe a month.&nbsp; Ramsey is still with us; happily adopted in June of 2017. He is just one of dozens of Labs we saved this year who prove that you don’t have to give up on a dog in need; that love and care can increase both the length and quality of a dog’s life and provide infinite joy for his family.</p>
    <p>When hospice care is needed we step up.&nbsp; When orthopedic issues, such as knee and hip&nbsp; surgeries, and arthritis medication are needed, we don’t hesitate. When dogs who have experienced years of neglect have a chance at a new life, we swoop in and save them.</p>
    <p><strong>We need your help to save every Lab we can.</strong></p>
    <p>This year we have gone even further, literally! We also rescued 26 Labs from hurricane-impacted areas of the United States.&nbsp; We couldn’t anticipate the need or plan for it but we found a way to save Labs displaced by the storms.</p>
    <p>Your financial support gives us the ability to say yes, every time<br>we’re needed.</p>
    <p>What’s involved in helping hurricane impacted dogs? A lot! From the moment that Hurricane Harvey touched down in Houston, Retriever Haven</p>
  </div>

  <div class="footer">
    <div class="contact">Lab Line: (555) 014-2290&nbsp; | P.O. Box 4420 Maplewood VA 20100</div>
    <div class="web">www.retrieverhaven.org</div>
  </div>
</div>
</body>
</html>
```